Quillmere Financial Plans

I am looking for a complete resdesign of my small financial presentation. This is a Word Doc/PDF that I print off when meeting with people in private. I often present my "two pager" that I have been using for years and years. It tells them the basics of what I do, how I help people and foundational financial principles.

I have recently gone out on my own in business and have completely rebranded. This presentation is my most used tool, so it is the first of many things I would like to redo. I am hoping it will somehow coordinate with the colors of my business, not necessarily the EXACT same 3 colors everywhere, but have the design colors compliment.

I've uploaded all my logo designs, as well as the current "two-pager". I am not against it going to 3 pages if needed. As it will still land on 2 pages with duplex printing.

It has always been VERY simple. I am wanting it built into a more professional and design specific format, to show off my branding, without being over cluttered.

I am completely open to ANY graphics changes. Obviously some are very novice, the house on the last page has always been overly simplified.

```html
<!DOCTYPE html>
<html lang="en">
<head>
<meta charset="utf-8">
<title>Quillmere Financial Plans – Two-Pager</title>
<link rel="stylesheet" href="https://fonts.googleapis.com/css2?family=Montserrat:wght@400;500;600;700;800&display=swap">
<style>
  :root{
    --green:#1cb24b;
    --navy:#0f2135;
    --grey:#8e9399;
    --grey-light:#f1f1f1;
    --cell:#f2f2f2;
    --text:#2b2f33;
    --maroon:#7a0f14;
    --pill:#d7ecf8;
    --icon:#2b4aa0;
    --backdrop:#e4e5e6;
  }
  *{box-sizing:border-box;margin:0;padding:0}
  html,body{width:842px;height:1200px;overflow:hidden;background:var(--backdrop)}
  body{font-family:"Montserrat",sans-serif;color:var(--text);position:relative}

  .sheet{position:absolute;left:210px;width:842px;height:1190px;background:#fff;transform:scale(.5);transform-origin:0 0;overflow:hidden}
  .sheet-one{top:3px}
  .sheet-two{top:602px}

  /* shared */
  .band{position:absolute;left:0;top:0;width:842px}
  .footer-band{position:absolute;left:0;bottom:0;width:842px;height:20px}
  .brand{position:absolute;text-align:center}
  .brand-name{font-weight:800;color:var(--navy);display:flex;align-items:center;justify-content:center;gap:10px;letter-spacing:1px}
  .brand-mark{border-radius:50%;background:var(--green)}
  .brand-sub{display:flex;align-items:center;justify-content:center;gap:12px;font-weight:700;color:var(--navy)}
  .brand-sub::before,.brand-sub::after{content:"";width:36px;height:2px;background:var(--navy)}

  /* page one */
  .page-title{position:absolute;left:76px;top:30px;color:#fff;font-weight:800;font-size:31px;line-height:34px;letter-spacing:.3px}
  .brand-main{left:430px;top:42px;width:340px}
  .brand-main .brand-name{font-size:44px}
  .brand-main .brand-mark{width:16px;height:16px}
  .brand-main .brand-sub{margin-top:6px;font-size:15px;letter-spacing:4px}

  .stat-label{position:absolute;left:60px;width:106px;height:35px;background:var(--navy);color:#fff;font-weight:700;font-size:15px;display:flex;align-items:center;justify-content:center;border-radius:4px}
  .stat-block{position:absolute;left:211px;width:577px;padding:12px 40px 12px 42px;border-radius:12px;font-size:12px;line-height:17px;color:#3a3e42}
  .stat-block.shaded{background:var(--grey-light)}
  .stat-block p{position:relative}
  .stat-block .tick{position:absolute;left:-24px;top:3px;width:11px;height:11px}
  .source{font-weight:700;color:#222}

  .services{position:absolute;left:61px;top:664px;width:345px;height:494px;border:4px solid var(--green);border-radius:20px;padding:24px 30px 0 38px}
  .services h2{font-weight:800;font-size:23px;line-height:24px;color:var(--green)}
  .services h2 span{color:var(--grey);display:block}
  .service-list{list-style:none;margin-top:14px}
  .service-list li{display:flex;align-items:center;height:66px;border-bottom:1.5px solid #e2e2e2;font-weight:700;font-size:14.5px;color:#1f2328;gap:22px;margin-left:-6px}
  .service-list li:last-child{border-bottom:none}
  .service-list svg{width:44px;height:40px;flex:none}

  .method-title{position:absolute;left:445px;top:685px;font-weight:800;font-size:25px;color:var(--grey)}
  .method-title span{color:var(--green)}
  .flow-box{position:absolute;left:434px;top:728px;width:354px;height:141px;border:3.5px solid var(--navy);border-radius:14px}
  .savings-word{position:absolute;left:148px;top:38px;font-weight:800;font-size:13px;color:#111}
  .goal-list{position:absolute;left:208px;top:20px;list-style:none;font-size:8.6px;font-weight:500;color:#222;text-transform:uppercase}
  .goal-list li{display:flex;align-items:center;gap:8px;height:25px}
  .goal-list li::before{content:"";width:12px;height:12px;border:1.6px solid var(--maroon)}

  .insurer-grid{position:absolute;left:434px;top:917px;display:grid;grid-template-columns:repeat(3,110px);grid-auto-rows:39px;column-gap:6px;row-gap:11px}
  .insurer{background:var(--pill);border:1px solid #b9dcf0;border-radius:9px;display:flex;align-items:center;justify-content:center;font-weight:700;font-size:11.5px;color:#1f3b73;text-align:center;line-height:12px;padding:0 4px}
  .pay-us{position:absolute;left:687px;top:1066px;width:94px;height:30px;background:var(--green);color:#fff;font-weight:800;font-size:17px;display:flex;align-items:center;justify-content:center;border-radius:3px}

  /* page two */
  .rule-title{position:absolute;left:0;width:842px;top:58px;text-align:center;font-weight:800;font-size:31px;color:var(--navy)}
  .rate-table{position:absolute;top:111px;width:183px;height:270px;border:2px solid var(--green)}
  .rate-head,.rate-row{display:grid;grid-template-columns:1fr 1fr;text-align:center;align-items:center}
  .rate-head{height:31px;background:var(--green);color:#fff;font-weight:700;font-size:14px}
  .rate-row{height:32px;background:var(--cell);margin-top:2px;font-weight:600;font-size:13px;color:#1f2328}
  .rate-note{position:absolute;top:399px;width:183px;height:53px;background:var(--cell);display:flex;align-items:center;justify-content:center;text-align:center;font-weight:600;font-size:13.5px;line-height:16px;color:#1f2328}

  .taxes-title{position:absolute;left:92px;top:520px;font-weight:800;font-size:37px;color:var(--navy)}
  .taxes-rule{position:absolute;left:44px;top:572px;width:182px;height:4px;background:var(--green)}
  .brand-small{left:575px;top:522px;width:222px}
  .brand-small .brand-name{font-size:31px;gap:7px}
  .brand-small .brand-mark{width:11px;height:11px}
  .brand-small .brand-sub{margin-top:3px;font-size:10.5px;letter-spacing:2.5px;gap:8px}
  .brand-small .brand-sub::before,.brand-small .brand-sub::after{width:24px}
  .roof-name{position:absolute;left:0;width:842px;top:620px;text-align:center;font-weight:800;font-size:24px;letter-spacing:2px;color:var(--grey)}

  .house-col{position:absolute;top:741px;width:159px}
  .house-head{height:35px;background:var(--green);color:#fff;font-weight:700;font-size:17px;display:flex;align-items:center;justify-content:center}
  .house-cell{height:36px;margin-top:5px;background:var(--cell);display:flex;align-items:center;justify-content:center;text-align:center;font-weight:500;font-size:11.5px;line-height:13px;color:#1f2328;padding:0 4px}
  .house-cell.tall{height:58px}
  .house-cell.empty{background:transparent}
  .house-result{position:absolute;top:946px;width:159px;height:34px;border:2px solid #c9c9c9;display:flex;align-items:center;justify-content:center;color:var(--green);font-weight:700;font-size:13px}
  .house-foot{position:absolute;width:330px;text-align:center;font-weight:700;font-size:17px}
  .house-foot.upper{top:1040px;color:var(--navy)}
  .house-foot.lower{top:1084px;color:var(--green)}
  .house-foot-rule{position:absolute;left:129px;top:1070px;width:618px;height:2px;background:var(--green)}
</style>
</head>
<body>

<!-- PAGE ONE -->
<main class="sheet sheet-one">
  <svg class="band" height="127" viewBox="0 0 842 127" aria-hidden="true">
    <polygon points="0,0 390,0 340,127 0,127" fill="var(--green)"/>
    <polygon points="408,0 842,0 842,11 404,11" fill="var(--grey)"/>
  </svg>
  <h1 class="page-title">THE FINANCIAL<br>CHALLENGE</h1>

  <div class="brand brand-main">
    <div class="brand-name"><span class="brand-mark"></span>QUILLMERE</div>
    <div class="brand-sub">FINANCIAL PLANS</div>
  </div>

  <div class="stat-label" style="top:212px">SAVINGS</div>
  <div class="stat-block shaded" style="top:148px;height:166px">
    <p><svg class="tick" viewBox="0 0 12 12"><circle cx="6" cy="6" r="6" fill="var(--green)"/><path d="M3.2 6.2l2 2 3.6-4" stroke="#fff" stroke-width="1.6" fill="none"/></svg>49% OF CANADIAN EMPLOYEES ARE LIVING PAYCHEQUE TO PAYCHEQUE. 25% OF CANADIANS ARE UNABLE TO COVER AN UNEXPECTED $500 EXPENSE<br><span class="source">- NATIONAL STATS BUREAU (FEB 2023)</span></p>
    <p><svg class="tick" viewBox="0 0 12 12"><circle cx="6" cy="6" r="6" fill="var(--green)"/><path d="M3.2 6.2l2 2 3.6-4" stroke="#fff" stroke-width="1.6" fill="none"/></svg>25% OF CANADIANS NEED TO ACCESS THEIR RETIREMENT SAVINGS EARLY. 20% OF CANADIANS HAVE NO SAVINGS.39% OF CANADIANS AGED 55-65 LESS THAN $5,000 IN SAVINGS.<br><span class="source">- FEDERAL FINANCE OFFICE (JUNE 2023)</span></p>
  </div>

  <div class="stat-label" style="top:373px">DEBT</div>
  <div class="stat-block" style="top:322px;height:140px">
    <p><svg class="tick" viewBox="0 0 12 12"><circle cx="6" cy="6" r="6" fill="var(--green)"/><path d="M3.2 6.2l2 2 3.6-4" stroke="#fff" stroke-width="1.6" fill="none"/></svg>THE AVERAGE CANADIAN HAS $22,131 IN CONSUMER DEBT. WHICH EXCLUDES MORTGAGES.<br><span class="source">- CREDITTRACK (AUG 2024)</span></p>
    <p><svg class="tick" viewBox="0 0 12 12"><circle cx="6" cy="6" r="6" fill="var(--green)"/><path d="M3.2 6.2l2 2 3.6-4" stroke="#fff" stroke-width="1.6" fill="none"/></svg>OVER 55% OF CANADIANS HOLD CREDIT CARD DEBT AND THE TOTAL CANADIAN HOUSEHOLD DEBT HAS INCREASED TO $2.52TRILLION, INCLUDING CONSUMER CREDIT, MORTGAGE AND NON-MORTGAGE LOANS.<br><span class="source">- BANKERS COUNCIL (AUG 2024)</span></p>
  </div>

  <div class="stat-label" style="top:541px">INSURANCE</div>
  <div class="stat-block shaded" style="top:472px;height:168px">
    <p><svg class="tick" viewBox="0 0 12 12"><circle cx="6" cy="6" r="6" fill="var(--green)"/><path d="M3.2 6.2l2 2 3.6-4" stroke="#fff" stroke-width="1.6" fill="none"/></svg>45% OF CANADIANS DO NOT HAVE INDIVIDUAL LIFE INSURANCE COVERAGE, BUT 48% SAY THEIR FAMILIES WOULD FACE FINANCIAL TROUBLE WITHIN 6 MONTHS OF LOSING SOMEONE.<br><span class="source">-INSURANCE RESEARCH INTL. (APR 2023)</span></p>
    <p><svg class="tick" viewBox="0 0 12 12"><circle cx="6" cy="6" r="6" fill="var(--green)"/><path d="M3.2 6.2l2 2 3.6-4" stroke="#fff" stroke-width="1.6" fill="none"/></svg>2-in-5 CANADIANS (43% WOMEN / 44% MEN) WILL BE DIAGOSED WITH A FORM OF CANCER OR OTHER CRITICAL ILLNESS DURING THEIR LIFETIME. EVERY 7 SECONDS.<br><span class="source">-HEALTH DATA REGISTRY (JUNE 2024)</span></p>
  </div>

  <section class="services">
    <h2>WHO ARE WE AND <span>WHAT DO WE DO?</span></h2>
    <ul class="service-list">
      <li><svg viewBox="0 0 44 40"><rect x="4" y="12" width="36" height="20" rx="2" fill="var(--icon)"/><rect x="8" y="16" width="28" height="12" fill="#fff"/><circle cx="22" cy="22" r="4" fill="var(--icon)"/><rect x="8" y="7" width="28" height="3" fill="var(--icon)"/></svg>CASH FLOW</li>
      <li><svg viewBox="0 0 44 40"><path d="M4 20 A18 16 0 0 1 40 20 Z" fill="var(--icon)"/><path d="M22 20 V33 a3 3 0 0 1 -6 0" stroke="var(--icon)" stroke-width="2.5" fill="none"/></svg>CASH FLOW PROTECTION</li>
      <li><svg viewBox="0 0 44 40"><rect x="4" y="8" width="34" height="24" rx="2" fill="none" stroke="var(--icon)" stroke-width="3"/><rect x="4" y="14" width="34" height="5" fill="var(--icon)"/><line x1="4" y1="36" x2="40" y2="4" stroke="var(--icon)" stroke-width="3"/></svg>DEBT MANAGEMENT</li>
      <li><svg viewBox="0 0 44 40"><rect x="3" y="10" width="26" height="20" rx="2" fill="var(--icon)"/><path d="M29 16 h7 l5 7 v7 h-12z" fill="var(--icon)"/><circle cx="11" cy="32" r="4" fill="var(--icon)" stroke="#fff" stroke-width="1.5"/><circle cx="33" cy="32" r="4" fill="var(--icon)" stroke="#fff" stroke-width="1.5"/><path d="M16 14 v12 M10 20 h12" stroke="#fff" stroke-width="3"/></svg>EMERGENCY FUND</li>
      <li><svg viewBox="0 0 44 40"><ellipse cx="22" cy="21" rx="16" ry="12" fill="var(--icon)"/><rect x="12" y="29" width="5" height="7" fill="var(--icon)"/><rect x="26" y="29" width="5" height="7" fill="var(--icon)"/><rect x="19" y="8" width="8" height="3" fill="var(--icon)"/></svg>BUILD WEALTH</li>
      <li><svg viewBox="0 0 44 40"><rect x="6" y="4" width="32" height="32" rx="2" fill="none" stroke="var(--icon)" stroke-width="3"/><rect x="11" y="9" width="22" height="22" fill="none" stroke="var(--icon)" stroke-width="2"/><circle cx="22" cy="20" r="4" fill="var(--icon)"/></svg>PRESERVE</li>
    </ul>
  </section>

  <h2 class="method-title">HOW ARE WE <span>DOING IT?</span></h2>
  <div class="flow-box">
    <svg style="position:absolute;left:12px;top:8px" width="118" height="118" viewBox="0 0 118 118" role="img" aria-label="Pie chart of income: living expenses, taxes, debt">
      <circle cx="59" cy="59" r="57" fill="var(--maroon)"/>
      <path d="M59 2 V116 M59 59 H116" stroke="#fff" stroke-width="1.5"/>
      <text x="30" y="56" font-size="8" fill="#fff" text-anchor="middle" font-family="Montserrat,sans-serif">Living</text>
      <text x="30" y="66" font-size="8" fill="#fff" text-anchor="middle" font-family="Montserrat,sans-serif">Expenses</text>
      <text x="88" y="42" font-size="8" fill="#fff" text-anchor="middle" font-family="Montserrat,sans-serif">Taxes</text>
      <text x="86" y="88" font-size="8" fill="#fff" text-anchor="middle" font-family="Montserrat,sans-serif">Debt</text>
    </svg>
    <span class="savings-word">SAVINGS</span>
    <svg style="position:absolute;left:152px;top:60px" width="50" height="10" viewBox="0 0 50 10" aria-hidden="true"><path d="M0 5 H44 M39 1 L45 5 L39 9" stroke="#333" stroke-width="1.3" fill="none"/></svg>
    <ul class="goal-list">
      <li>Retirement Savings</li>
      <li>Children's Education</li>
      <li>Proper Protection</li>
      <li>Freedom From Debt</li>
    </ul>
  </div>
  <svg style="position:absolute;left:600px;top:870px" width="14" height="36" viewBox="0 0 14 36" aria-hidden="true"><path d="M7 0 V28" stroke="var(--navy)" stroke-width="2.5"/><path d="M1 24 L7 34 L13 24Z" fill="var(--navy)"/></svg>

  <div class="insurer-grid">
    <div class="insurer">Maplewell</div>
    <div class="insurer">Harborlife</div>
    <div class="insurer">Brightfield Financial</div>
    <div class="insurer">Northcrest Group</div>
    <div class="insurer">Lakeshore Mutual</div>
    <div class="insurer">Pinecrest Insurance</div>
    <div class="insurer">Valora</div>
    <div class="insurer">Ridgeway Insurance</div>
    <div></div>
    <div class="insurer">Unity Mutual</div>
    <div class="insurer">Solenne</div>
  </div>
  <svg style="position:absolute;left:727px;top:1018px" width="14" height="38" viewBox="0 0 14 38" aria-hidden="true"><path d="M7 0 V30" stroke="var(--navy)" stroke-width="2"/><path d="M1 26 L7 36 L13 26" stroke="var(--navy)" stroke-width="2" fill="none"/></svg>
  <div class="pay-us">PAY US</div>

  <svg class="footer-band" viewBox="0 0 842 20" aria-hidden="true">
    <polygon points="452,0 842,0 842,20 442,20" fill="var(--navy)"/>
  </svg>
</main>

<!-- PAGE TWO -->
<main class="sheet sheet-two">
  <svg class="band" height="14" viewBox="0 0 842 14" aria-hidden="true">
    <polygon points="0,0 418,0 413,14 0,14" fill="var(--green)"/>
    <polygon points="430,0 842,0 842,14 425,14" fill="var(--grey)"/>
  </svg>

  <h2 class="rule-title">RULE OF 72</h2>

  <div class="rate-table" style="left:43px">
    <div class="rate-head"><span>AGE</span><span>4%</span></div>
    <div class="rate-row"><span>29</span><span>$10,000</span></div>
    <div class="rate-row"><span>47</span><span>$20,000</span></div>
    <div class="rate-row"><span>65</span><span>$40,000</span></div>
  </div>
  <div class="rate-table" style="left:233px">
    <div class="rate-head"><span>AGE</span><span>6%</span></div>
    <div class="rate-row"><span>29</span><span>$10,000</span></div>
    <div class="rate-row"><span>41</span><span>$20,000</span></div>
    <div class="rate-row"><span>53</span><span>$40,000</span></div>
    <div class="rate-row"><span>65</span><span>$80,000</span></div>
  </div>
  <div class="rate-table" style="left:424px">
    <div class="rate-head"><span>AGE</span><span>8%</span></div>
    <div class="rate-row"><span>29</span><span>$10,000</span></div>
    <div class="rate-row"><span>38</span><span>$20,000</span></div>
    <div class="rate-row"><span>47</span><span>$40,000</span></div>
    <div class="rate-row"><span>56</span><span>$80,000</span></div>
    <div class="rate-row"><span>65</span><span>$160,000</span></div>
  </div>
  <div class="rate-table" style="left:614px">
    <div class="rate-head"><span>AGE</span><span>12%</span></div>
    <div class="rate-row"><span>29</span><span>$10,000</span></div>
    <div class="rate-row"><span>35</span><span>$20,000</span></div>
    <div class="rate-row"><span>41</span><span>$40,000</span></div>
    <div class="rate-row"><span>47</span><span>$80,000</span></div>
    <div class="rate-row"><span>53</span><span>$160,000</span></div>
    <div class="rate-row"><span>59</span><span>$320,000</span></div>
    <div class="rate-row"><span>59</span><span>$640,000</span></div>
  </div>

  <div class="rate-note" style="left:43px">MONEY DOUBLES<br>EVERY 6 YEARS</div>
  <div class="rate-note" style="left:233px">MONEY DOUBLES<br>EVERY 9 YEARS</div>
  <div class="rate-note" style="left:424px">MONEY DOUBLES<br>EVERY 12 YEARS</div>
  <div class="rate-note" style="left:614px">MONEY DOUBLES<br>EVERY 18 YEARS</div>

  <h2 class="taxes-title">TAXES</h2>
  <div class="taxes-rule"></div>

  <div class="brand brand-small">
    <div class="brand-name"><span class="brand-mark"></span>QUILLMERE</div>
    <div class="brand-sub">FINANCIAL PLANS</div>
  </div>

  <svg style="position:absolute;left:0;top:0" width="842" height="1190" viewBox="0 0 842 1190" aria-hidden="true">
    <polygon points="419,545 10,707 832,707" fill="none" stroke="var(--navy)" stroke-width="4" stroke-linejoin="miter"/>
    <polyline points="57,707 57,1130 785,1130 785,707" fill="none" stroke="var(--navy)" stroke-width="4"/>
    <line x1="57" y1="1018" x2="785" y2="1018" stroke="var(--navy)" stroke-width="4"/>
  </svg>
  <div class="roof-name">QUILLMERE</div>

  <div class="house-col" style="left:91px">
    <div class="house-head">HOME</div>
    <div class="house-cell tall">PARTNER WITH<br>MORTGAGE BROKERS<br>FOR BEST RATES</div>
    <div class="house-cell tall">MORTGAGE<br>INSURANCE<br>ALTERNATIVES</div>
  </div>
  <div class="house-col" style="left:258px">
    <div class="house-head">RRSP</div>
    <div class="house-cell">TAX DEDUCTION</div>
    <div class="house-cell">TAX DEFERRED</div>
  </div>
  <div class="house-col" style="left:425px">
    <div class="house-head">TFSA</div>
    <div class="house-cell">NO TAX DEDUCTIONS</div>
    <div class="house-cell">TAX FREE GROWTH</div>
    <div class="house-cell">2009 - $95,000</div>
    <div class="house-cell">LIMIT 2023 - $7,000/YR</div>
  </div>
  <div class="house-col" style="left:591px">
    <div class="house-head">PERM LIFE</div>
    <div class="house-cell">NO TAX DEDUCTION</div>
    <div class="house-cell">QUALIFY</div>
    <div class="house-cell">TAX DEFERRED GROWTH</div>
    <div class="house-cell">TAX DEDCTION</div>
  </div>

  <div class="house-result" style="left:91px">SELL</div>
  <div class="house-result" style="left:258px">100% TAX</div>
  <div class="house-result" style="left:425px">100% TAX</div>
  <div class="house-result" style="left:591px">0% TAX</div>

  <div class="house-foot upper" style="left:87px">LIFE INSURANCE ILLNESS</div>
  <div class="house-foot upper" style="left:419px">DEBT MANAGEMENT</div>
  <div class="house-foot-rule"></div>
  <div class="house-foot lower" style="left:87px">CRITICAL/DISABILITY</div>
  <div class="house-foot lower" style="left:419px">CASH FLOW</div>

  <svg class="footer-band" viewBox="0 0 842 20" aria-hidden="true">
    <polygon points="452,0 842,0 842,20 442,20" fill="var(--navy)"/>
  </svg>
</main>

</body>
</html>
```